IT Consulting Site Revamping for Marlune

I've put a skeleton together on my website, but realize I need some help (it's http://pilot.marlune-example.ca).
I've pulled together tidbits from other websites, but really need my site to be cleaned up, and really spruced up.
I primarily focus on the IT needs of small to medium size businesses, taking care of everything from their servers and networks down to their workstations.
I also want a page listing the vendors (and logos) that I work with including Quillsoft, Zentrix, Halvor, Brax, TL, RZO, VELK, Trevo, Gatemoor.
There should also be a simple form to get a quote that will email me.
The final design should communicate strength and reliability.
I would like this to be a fully functional website, that I can upload to Plumly Pages, with the same sort of pages that are existing on http://pilot.marlune-example.ca
Updates
Hey everyone,
Hi everyone,
Reason: Hi all,
There are some designers that would like to submit some new designs, so I'm extending the deadline.
Thanks,
Target Market(s)
Small to medium size business owners. This will primarily be males who work in the oil and gas industry.
Industry/Entity Type
Consulting
Look and feel
Each slider illustrates characteristics of the customer's brand and the style your logo design should communicate.

```html
<!DOCTYPE html>
<html lang="en">
<head>
<meta charset="utf-8">
<title>Marlune Solutions</title>
<link href="https://fonts.googleapis.com/css2?family=Ubuntu:wght@300;400;500;700&family=PT+Sans:ital,wght@0,400;0,700;1,700&family=Arimo:wght@400&display=swap" rel="stylesheet">
<style>
:root{
  --bg:#f4f3ef;
  --blue:#1a8ed0;
  --blue-dark:#0d6fae;
  --blue-light:#3eaee6;
  --ink:#1d1d1d;
  --body:#2f2f2f;
  --muted:#555;
  --rule:#cfcfcf;
  --footer:#2b2b2b;
  --footer-text:#d8d8d8;
  --nav-dark:#3a3a3a;
}
*{margin:0;padding:0;box-sizing:border-box}
html,body{width:1108px;height:1200px;overflow:hidden;background:var(--bg)}
body{position:relative;font-family:"PT Sans",sans-serif;color:var(--body)}
.abs{position:absolute}

/* header */
.brand{left:94px;top:18px;display:flex;align-items:center;gap:14px}
.brand-dot{width:78px;height:78px;border-radius:50%;background:var(--blue)}
.brand-name{font-family:"Ubuntu",sans-serif;font-weight:500;font-size:44px;color:var(--blue);letter-spacing:-1px}
.phone{right:93px;top:8px;display:flex;align-items:center;gap:8px}
.phone-text{font-family:"Ubuntu",sans-serif;font-weight:300;font-size:31px;color:#3b3b3b;letter-spacing:2px}
.connect{right:93px;top:84px;display:flex;align-items:center;gap:8px}
.connect-label{font-family:"Ubuntu",sans-serif;font-weight:300;font-size:19px;color:#555;margin-right:4px}
.social{width:32px;height:32px;border-radius:50%;background:#d6d6d6;border:2px solid #fff;box-shadow:0 1px 3px rgba(0,0,0,.3)}
.social.blue{background:#3b6db3}.social.sky{background:#3aa4dc}.social.orange{background:#e0791e}.social.grey{background:#cfcfcf}

/* nav */
.nav{left:0;top:132px;width:1108px;height:36px;background:linear-gradient(#3eaee6,#1584c6);box-shadow:0 1px 2px rgba(0,0,0,.2)}
.nav-home{left:102px;top:125px;width:87px;height:50px;background:linear-gradient(#555,#262626);border-radius:4px;box-shadow:inset 0 0 0 4px #1b1b1b}
.nav-item{top:142px;font-family:"Arimo",sans-serif;font-size:14.5px;color:#fff}
.nav-sep{top:132px;width:1px;height:36px;background:rgba(255,255,255,.25);box-shadow:1px 0 0 rgba(0,0,0,.12)}

/* slider */
.slider{left:118px;top:200px;width:856px;height:315px;background:#fff;border-radius:10px;box-shadow:0 1px 3px rgba(0,0,0,.15)}
.slide-photo{left:139px;top:206px;width:830px;height:304px;background:linear-gradient(90deg,#dfe6ee 0%,#f7f9fb 40%,#e6e9ec 60%,#c9ccd1 100%)}
.slide-shadow{left:170px;top:515px;width:760px;height:18px;background:radial-gradient(ellipse at top,rgba(0,0,0,.22),rgba(0,0,0,0) 70%)}
.arrow{top:342px;width:47px;height:40px;background:linear-gradient(#3d3d3d,#141414);display:flex;align-items:center;justify-content:center}
.arrow.prev{left:105px;border-radius:0 20px 20px 0}
.arrow.next{left:939px;border-radius:20px 0 0 20px}
.dots{left:507px;top:501px;width:100px;height:26px;background:#fff;border-radius:13px;box-shadow:0 1px 3px rgba(0,0,0,.35);display:flex;align-items:center;justify-content:center;gap:3px}
.dot{width:10px;height:10px;border-radius:50%;background:#888}
.dot.on{background:#fff;border:2px solid #888}

/* sections */
.section-icon{border-radius:50%;background:var(--blue)}
.heading{font-family:"Ubuntu",sans-serif;font-weight:400;color:var(--ink)}
.heading span{color:var(--blue)}
.about-rule{left:166px;top:606px;width:767px;border-top:1px dotted var(--rule)}
.about-text{left:113px;width:862px;font-size:10.6px;line-height:16.6px;color:var(--body)}
.about-text b{font-style:italic}
.more{display:flex;align-items:center;gap:5px;font-size:11px;color:#3a3a3a}
.plus{width:21px;height:21px;border-radius:50%;background:radial-gradient(circle at 40% 35%,#5cc1f2,#127cc2);display:flex;align-items:center;justify-content:center}

/* services */
.services{left:111px;top:821px;width:884px;height:233px;border:1px dotted #777;border-bottom:none;display:flex}
.service{position:relative;flex:1;border-right:1px dotted #777;padding:11px 0 0 12px}
.service:last-child{border-right:none}
.service-photo{width:189px;height:102px;border:3px solid #fff;box-shadow:0 1px 4px rgba(0,0,0,.3)}
.service-title{font-family:"Ubuntu",sans-serif;font-weight:500;font-size:18.5px;color:#1c9bd8;margin:10px 0 0 4px;white-space:nowrap}
.service-title span{color:#2e2e2e}
.service-text{font-family:"Arimo",sans-serif;font-size:11px;line-height:16.6px;letter-spacing:.3px;color:#444;margin:2px 0 0 4px;width:180px;text-align:justify}
.service .more{position:absolute;right:12px;bottom:4px}

/* footer */
.footer{left:0;top:1080px;width:1108px;height:120px;background:var(--footer)}
.footer-brand{left:94px;top:1108px;display:flex;align-items:center;gap:12px}
.footer-dot{width:66px;height:66px;border-radius:50%;background:#8a8a8a}
.footer-name{font-family:"Ubuntu",sans-serif;font-weight:500;font-size:36px;color:#8a8a8a;letter-spacing:-1px}
.footer-links{left:300px;top:1125px;width:502px;text-align:center;font-family:"Arimo",sans-serif;font-size:11px;letter-spacing:.6px;color:var(--footer-text);line-height:19px}
.footer-links i{font-style:normal;margin:0 12px}
.footer-contact{right:106px;top:1118px;text-align:right;font-family:"Arimo",sans-serif;font-size:11px;letter-spacing:.6px;color:var(--footer-text);line-height:18.5px}
</style>
</head>
<body>

<header>
  <div class="abs brand"><div class="brand-dot"></div><div class="brand-name">Marlune</div></div>
  <div class="abs phone">
    <svg width="36" height="36" viewBox="0 0 36 36"><circle cx="18" cy="18" r="17" fill="#1a7fc2"/><path d="M12 10c-2 2-2 6 2 11s8 6 10 4l1-2-4-3-2 2c-2-1-4-3-5-5l2-2-3-4z" fill="#fff"/></svg>
    <span class="phone-text">08 5550 1842</span>
  </div>
  <div class="abs connect">
    <span class="connect-label">Connect with us -:</span>
    <span class="social blue"></span><span class="social sky"></span><span class="social orange"></span><span class="social grey"></span>
  </div>
</header>

<nav>
  <div class="abs nav"></div>
  <div class="abs nav-home"></div>
  <span class="abs nav-item" style="left:128px">Home</span>
  <span class="abs nav-sep" style="left:205px"></span>
  <span class="abs nav-item" style="left:228px">About us</span>
  <span class="abs nav-sep" style="left:322px"></span>
  <span class="abs nav-item" style="left:353px">Our Services</span>
  <span class="abs nav-sep" style="left:466px"></span>
  <span class="abs nav-item" style="left:492px">Our Products</span>
  <span class="abs nav-sep" style="left:611px"></span>
  <span class="abs nav-item" style="left:632px">Contact us</span>
</nav>

<section class="hero">
  <div class="abs slide-shadow"></div>
  <div class="abs slider"></div>
  <div class="abs slide-photo" role="img" aria-label="Photo of a smiling support agent with a headset and two colleagues reviewing work on a laptop"></div>
  <div class="abs arrow prev"><svg width="12" height="14" viewBox="0 0 12 14"><path d="M2 1l7 6-7 6" stroke="#fff" stroke-width="3" fill="none"/></svg></div>
  <div class="abs arrow next"><svg width="12" height="14" viewBox="0 0 12 14"><path d="M10 1L3 7l7 6" stroke="#fff" stroke-width="3" fill="none"/></svg></div>
  <div class="abs dots"><span class="dot on"></span><span class="dot"></span><span class="dot"></span><span class="dot"></span><span class="dot"></span></div>
</section>

<section class="about">
  <div class="abs section-icon" style="left:109px;top:558px;width:52px;height:52px"></div>
  <h2 class="abs heading" style="left:166px;top:566px;font-size:24px">About <span>Company</span></h2>
  <div class="abs about-rule"></div>
  <p class="abs about-text" style="top:624px"><b>Lorem ipsum dolor sit amet, sit lectus blandit non nec egestas nulla, ac ut vitae massa blanditiis pulvinar, aenean enim nec sapien quis velit nunc, nunc fugiat velit purus ligula. In mattis curabitur id at aliquam, pede eu in massa nibh porttitor.</b> Tellus vestibulum nulla nunc nascetur nec, vestibulum ac malesuada velit tempus. Et iaculis ultricies, sapien sapien vitae odio, rutrum arcu. Vitae porttitor dapibus lacus id enim, in nulla, fermentum nec torquent ut erat habitasse.</p>
  <p class="abs about-text" style="top:691px">Cras felis enim, purus ut turpis, et lacus suspendisse, nullam a curabitur. Pede risus duis, et metus nisl metus pharetra. Et lacinia eget mauris morbi urna esse, pede phasellus leo veniam ut justo. Id arcu cum semper tempus, eget lacus, phasellus conubia duis. Odio nibh hymenaeos laudantium at aptent, voluptate laoreet erat vel dignissim justo.</p>
  <a class="abs more" style="left:904px;top:742px">View More <span class="plus"><svg width="11" height="11"><path d="M5.5 0v11M0 5.5h11" stroke="#fff" stroke-width="2.4"/></svg></span></a>
</section>

<section class="our-services">
  <div class="abs section-icon" style="left:112px;top:779px;width:29px;height:29px"></div>
  <h2 class="abs heading" style="left:145px;top:780px;font-size:22px">Our <span>Services</span></h2>
  <div class="abs services">
    <article class="service">
      <div class="service-photo" role="img" aria-label="Photo of a business team standing in a server room" style="background:linear-gradient(90deg,#e9ecef,#cfd6de 55%,#3c4a66 80%,#9aa6b4)"></div>
      <h3 class="service-title">Managed IT <span>Services</span></h3>
      <p class="service-text">Quis cum nibh tellus, dapibus est duis felis id proin molestie, duis tortor amet quam amet nec...</p>
      <a class="more">View More <span class="plus"><svg width="11" height="11"><path d="M5.5 0v11M0 5.5h11" stroke="#fff" stroke-width="2.4"/></svg></span></a>
    </article>
    <article class="service">
      <div class="service-photo" role="img" aria-label="Photo of a technician working among network cables" style="background:linear-gradient(90deg,#1a2f7a,#2f5bd0 50%,#4a6aa8 70%,#1c2a55)"></div>
      <h3 class="service-title">Networking <span>Services</span></h3>
      <p class="service-text">Quis cum nibh tellus, dapibus est duis felis id proin molestie, duis tortor amet quam amet nec...</p>
      <a class="more">View More <span class="plus"><svg width="11" height="11"><path d="M5.5 0v11M0 5.5h11" stroke="#fff" stroke-width="2.4"/></svg></span></a>
    </article>
    <article class="service">
      <div class="service-photo" role="img" aria-label="Close-up photo of a USB flash drive" style="background:linear-gradient(135deg,#9a9a9a,#d9d9d9 45%,#555 70%,#bdbdbd)"></div>
      <h3 class="service-title">Recovery <span>Backups</span></h3>
      <p class="service-text">Quis cum nibh tellus, dapibus est duis felis id proin molestie, duis tortor amet quam amet nec...</p>
      <a class="more">View More <span class="plus"><svg width="11" height="11"><path d="M5.5 0v11M0 5.5h11" stroke="#fff" stroke-width="2.4"/></svg></span></a>
    </article>
    <article class="service">
      <div class="service-photo" role="img" aria-label="Photo of a computer lab with rows of monitors" style="background:linear-gradient(#6f8fd6,#2c4a94 50%,#0e1a3c)"></div>
      <h3 class="service-title">Computer <span>Services</span></h3>
      <p class="service-text">Quis cum nibh tellus, dapibus est duis felis id proin molestie, duis tortor amet quam amet nec...</p>
      <a class="more">View More <span class="plus"><svg width="11" height="11"><path d="M5.5 0v11M0 5.5h11" stroke="#fff" stroke-width="2.4"/></svg></span></a>
    </article>
  </div>
</section>

<footer>
  <div class="abs footer"></div>
  <div class="abs footer-brand"><div class="footer-dot"></div><div class="footer-name">Marlune</div></div>
  <div class="abs footer-links">Home<i>|</i>About Us<i>|</i>Our Services<i>|</i>Our Products<i>|</i>Contact us<br>© 2012 Marlune Solutions. Inc. All rights reserved.</div>
  <div class="abs footer-contact">Telephone (02) 5550 1510<br>Facsimile (02) 5550 1620<br>Email info@marlune-example.ca</div>
</footer>

</body>
</html>
```